brix4lane

i want to ues this logo and the same colors used on the business card

cleaning & service

Industry/Entity Type

Business

Contact Information for Business Card

Font styles to use
Serif
Sans Serif
Decorative
Script

Colors
add136
0692cd
000000
5c5c5c
fbfbfb

Requirements
Must have
• cleaning things

```html
<!DOCTYPE html>
<html lang="en">
<head>
<meta charset="utf-8">
<title>brix4lane — Business Card</title>
<link rel="stylesheet" href="https://fonts.googleapis.com/css2?family=Montserrat:wght@400;500;700&display=swap">
<style>
  :root {
    --brand-blue: #0a72bf;
    --brand-green: #add136;
    --paper: #ffffff;
    --backdrop: #e9eaec;
    --ink-white: #fbfbfb;
    --shadow: rgba(0, 0, 0, 0.18);
  }
  * { box-sizing: border-box; margin: 0; padding: 0; }
  html, body { width: 1200px; height: 900px; overflow: hidden; }
  body {
    background: var(--backdrop);
    font-family: "Montserrat", Arial, sans-serif;
    position: relative;
  }
  .card {
    position: absolute;
    left: 300px;
    width: 600px;
    height: 343px;
    background: var(--paper);
    box-shadow: 0 8px 24px var(--shadow);
    overflow: hidden;
  }
  .card--front { top: 70px; }
  .card--back { top: 487px; }

  .brand-mark {
    position: absolute;
    display: flex;
    align-items: center;
    gap: 12px;
    color: var(--brand-blue);
    font-weight: 700;
    font-size: 40px;
    letter-spacing: 0.5px;
  }
  .brand-mark__dot {
    width: 18px; height: 18px;
    border-radius: 50%;
    background: var(--brand-green);
  }
  .card--front .brand-mark {
    left: 50%; top: 50%;
    transform: translate(-50%, -50%);
  }
  .card--back .brand-mark {
    left: 110px; top: 235px;
    font-size: 34px;
  }

  .back-shapes { position: absolute; inset: 0; width: 600px; height: 343px; }
  .back-shapes .fill { fill: var(--brand-blue); }

  .contact {
    position: absolute;
    right: 38px; top: 38px;
    text-align: right;
    color: var(--ink-white);
  }
  .contact__name {
    font-size: 19px;
    font-weight: 700;
    letter-spacing: 0.3px;
  }
  .contact__name .surname { color: var(--brand-green); }
  .contact__role {
    font-size: 12px;
    font-weight: 400;
    margin-top: 2px;
    margin-bottom: 16px;
  }
  .contact__line {
    display: flex;
    justify-content: flex-end;
    align-items: center;
    gap: 8px;
    font-size: 13px;
    font-weight: 500;
    margin-top: 7px;
  }
  .contact__icon { width: 13px; height: 13px; fill: var(--brand-green); }
</style>
</head>
<body>

  <section class="card card--front">
    <div class="brand-mark"><span class="brand-mark__dot"></span>brix4lane</div>
  </section>

  <section class="card card--back">
    <svg class="back-shapes" viewBox="0 0 600 343" aria-hidden="true">
      <path class="fill" d="M0 0 H600 V252 C440 222 240 170 0 88 Z"/>
      <path class="fill" d="M360 236 C450 254 540 264 600 264 V274 C520 276 440 262 360 236 Z"/>
    </svg>

    <div class="contact">
      <p class="contact__name">NORA <span class="surname">VANDELL</span></p>
      <p class="contact__role">General Manager</p>
      <p class="contact__line">(555) 214-3087
        <svg class="contact__icon" viewBox="0 0 24 24" aria-hidden="true"><path d="M6.6 10.8a15.1 15.1 0 0 0 6.6 6.6l2.2-2.2a1 1 0 0 1 1-.25 11.4 11.4 0 0 0 3.6.57 1 1 0 0 1 1 1V20a1 1 0 0 1-1 1A17 17 0 0 1 3 4a1 1 0 0 1 1-1h3.5a1 1 0 0 1 1 1c0 1.25.2 2.45.57 3.57a1 1 0 0 1-.25 1z"/></svg>
      </p>
      <p class="contact__line">nora.vandell@mailbox.com
        <svg class="contact__icon" viewBox="0 0 24 24" aria-hidden="true"><path d="M2 5h20v14H2z M3.5 6.5 12 13l8.5-6.5" fill="var(--brand-green)"/><path d="M3 6l9 7 9-7" fill="none" stroke="var(--brand-blue)" stroke-width="1.8"/></svg>
      </p>
    </div>

    <div class="brand-mark"><span class="brand-mark__dot"></span>brix4lane</div>
  </section>

</body>
</html>
```